looking for sleek business card to standout from the crowd!

We are a young biotechnology company looking to help you personalize your health through understanding your genetic make up. We need you help in making a clean but sleek business card design using our new logo. The goal? Any time we give our cards out, people say "nice card!" The feel we are going for is "modern-techy". We don't want to come across as an old, giant pharma company, but not trying to be a hipster either.

Target Market(s)

healthcare and biotechnology industry.

Industry/Entity Type

Biotechnology

Contact Information for Business Card

Info to include on the card will be NAME, TITLE, EMAIL, PHONE. The companies website (www.corvalinbio.com) should also be on the card some where. Would like the logo, when printed, to be raised.

Requirements
Must have
• The logo we have attached in the color it is in. Fonts for text should lean toward more professional/tech.
Nice to have
• Prefer white/light color background
Should not have
• cartoons, landscape backgrounds images.

```html
<!DOCTYPE html>
<html lang="en">
<head>
<meta charset="utf-8">
<title>Corvalin Business Card</title>
<link href="https://fonts.googleapis.com/css2?family=Lora:wght@400;500&display=swap" rel="stylesheet">
<style>
  :root {
    --backdrop: #1b1b1f;
    --card: #ffffff;
    --brand-blue: #0a72b8;
    --brand-green: #7dc243;
    --rule-blue: #c6dcee;
    --helix-blue: #d3e4f3;
    --helix-green: #e6f2d6;
  }
  * { margin: 0; padding: 0; box-sizing: border-box; }
  html, body {
    width: 1200px; height: 960px; overflow: hidden;
    background: var(--backdrop);
    font-family: "Lora", Georgia, serif;
  }
  .card {
    position: absolute; left: 130px; top: 225px;
    width: 940px; height: 510px;
    background: var(--card);
    overflow: hidden;
  }
  .identity { position: absolute; left: 90px; top: 100px; }
  .identity__name {
    color: var(--brand-blue); font-size: 50px; font-weight: 400;
    letter-spacing: 1px; line-height: 1;
  }
  .identity__title {
    color: var(--brand-green); font-size: 24px; letter-spacing: 0.5px;
    margin-top: 6px;
  }
  .contacts { position: absolute; left: 90px; top: 265px; list-style: none; }
  .contacts__item {
    display: flex; align-items: center; gap: 22px;
    color: var(--brand-blue); font-size: 24px; height: 50px;
  }
  .contacts__icon { width: 26px; height: 26px; flex: none; fill: var(--brand-green); }
  .divider {
    position: absolute; left: 460px; top: 150px;
    width: 4px; height: 300px; background: var(--rule-blue);
  }
  .helix {
    position: absolute; left: 700px; top: 60px; width: 170px; height: 520px;
    background: linear-gradient(200deg, var(--helix-green) 0%, var(--helix-green) 35%, var(--helix-blue) 60%, var(--helix-blue) 100%);
    border-radius: 85px;
    transform: rotate(22deg);
    opacity: 0.85;
  }
  .brand {
    position: absolute; left: 515px; top: 258px;
    display: flex; align-items: center; gap: 14px;
  }
  .brand__name {
    color: var(--brand-blue); font-size: 54px; font-weight: 500;
    letter-spacing: 2px; line-height: 1;
  }
  .brand__dot {
    width: 50px; height: 50px; border-radius: 50%; background: var(--brand-green);
  }
</style>
</head>
<body>
  <main class="card">
    <div class="identity">
      <h1 class="identity__name">YOUR NAME</h1>
      <p class="identity__title">DESIGNATION</p>
    </div>

    <ul class="contacts">
      <li class="contacts__item">
        <svg class="contacts__icon" viewBox="0 0 24 24"><path d="M6.6 10.8a15.1 15.1 0 0 0 6.6 6.6l2.2-2.2a1 1 0 0 1 1-.25 11.4 11.4 0 0 0 3.6.57 1 1 0 0 1 1 1V20a1 1 0 0 1-1 1A17 17 0 0 1 3 4a1 1 0 0 1 1-1h3.5a1 1 0 0 1 1 1c0 1.25.2 2.450.57 3.57a1 1 0 0 1-.25 1z"/></svg>
        <span>5550-1427-7893</span>
      </li>
      <li class="contacts__item">
        <svg class="contacts__icon" viewBox="0 0 24 24"><path d="M2 5h20v14H2z M2 5l10 8 10-8" fill="none" stroke="#7dc243" stroke-width="2.5" stroke-linejoin="round"/></svg>
        <span>info@corvalinbio.com</span>
      </li>
      <li class="contacts__item">
        <svg class="contacts__icon" viewBox="0 0 24 24"><rect x="6" y="2" width="12" height="20" rx="6"/><rect x="11" y="3" width="2" height="8" fill="#fff"/><rect x="6" y="10" width="12" height="2" fill="#fff"/></svg>
        <span>www.corvalinbio.com</span>
      </li>
    </ul>

    <div class="divider"></div>

    <div class="helix" role="img" aria-label="Faint DNA double helix decoration in pale blue and green"></div>

    <div class="brand">
      <span class="brand__name">CORVALIN</span>
      <span class="brand__dot"></span>
    </div>
  </main>
</body>
</html>
```